Business cards for the RT Group

We are looking for a template for our new business cards for our company that we can edit ourselves.
You will find our company colors in the logo. the logo on the back and on the front
first name Last Name
position
E-mail address
mobile number
landline number
Companies we have 2 RT Sicherheit GmbH and RT Services GmbH
address
Lindauer Weg 42
22543 Hamburg
www.rtverbund-beispiel.de

Something modern, simple but professional

if you have any questions, bring it on.

Industry/Entity Type

Sicherheit

Contact Information for Business Card

Steht in der Beschreibung

Colors
F0912C
F2A743
F7CA91
FBE8D2
FDF5EE

Requirements
Must have
• recognition value
Nice to have
• professional
Should not have
• Playful

```html
<!DOCTYPE html>
<html lang="de">
<head>
<meta charset="utf-8">
<title>RT Gruppe – Visitenkarten</title>
<link href="https://fonts.googleapis.com/css2?family=Montserrat:wght@400;500;600;700;800&display=swap" rel="stylesheet">
<style>
  :root {
    --stage: #2b2b2e;
    --card-dark: #5e5e60;
    --card-light: #fbfbfa;
    --ink: #3c3c3e;
    --ink-soft: #4a4a4c;
    --orange: #f0912c;
    --orange-soft: #f7ca91;
    --mark-light: #c9c9cb;
    --watermark: #f1f1f0;
  }
  * { box-sizing: border-box; margin: 0; padding: 0; }
  html, body { width: 1200px; height: 900px; overflow: hidden; }
  body {
    background: var(--stage);
    font-family: "Montserrat", sans-serif;
    display: flex;
    align-items: center;
    justify-content: center;
    gap: 40px;
  }
  .card {
    position: relative;
    width: 540px;
    height: 310px;
    border-radius: 22px;
    overflow: hidden;
  }

  /* Back side */
  .card--back {
    background: var(--card-dark);
    display: flex;
    align-items: center;
    justify-content: center;
  }
  .brand {
    display: flex;
    align-items: center;
    gap: 16px;
  }
  .brand__dot {
    width: 34px;
    height: 34px;
    border-radius: 50%;
    background: var(--orange);
  }
  .brand__name {
    font-weight: 800;
    font-size: 54px;
    letter-spacing: 2px;
    color: var(--mark-light);
    line-height: 1;
  }

  /* Front side */
  .card--front { background: var(--card-light); }
  .watermark {
    position: absolute;
    left: -40px;
    top: 150px;
    width: 230px;
    height: 230px;
    border-radius: 50%;
    background: var(--watermark);
  }
  .front__brand {
    position: absolute;
    right: 36px;
    top: 38px;
    gap: 12px;
  }
  .front__brand .brand__dot { width: 22px; height: 22px; }
  .front__brand .brand__name {
    font-size: 36px;
    color: var(--ink);
  }
  .divider {
    position: absolute;
    left: 150px;
    right: 30px;
    top: 152px;
    height: 1.5px;
    background: var(--orange);
  }
  .person {
    position: absolute;
    left: 34px;
    top: 112px;
  }
  .person__name {
    font-weight: 700;
    font-size: 24px;
    color: var(--orange);
    line-height: 1.05;
  }
  .person__role {
    font-weight: 500;
    font-size: 12.5px;
    color: var(--ink-soft);
    margin-top: 2px;
  }
  .person__rule {
    width: 150px;
    height: 1.5px;
    background: var(--orange);
    margin-top: 10px;
  }
  .contact {
    position: absolute;
    left: 34px;
    top: 178px;
    list-style: none;
  }
  .contact__item {
    display: flex;
    align-items: center;
    gap: 10px;
    font-size: 13px;
    font-weight: 500;
    color: var(--ink);
    height: 24px;
  }
  .contact__icon { width: 13px; height: 13px; flex: none; }
  .address {
    position: absolute;
    right: 36px;
    top: 200px;
    text-align: right;
    font-size: 13px;
    font-weight: 500;
    color: var(--ink);
    line-height: 1.35;
  }
</style>
</head>
<body>

  <section class="card card--back" aria-label="Rückseite">
    <div class="brand">
      <span class="brand__dot"></span>
      <span class="brand__name">RT Gruppe</span>
    </div>
  </section>

  <section class="card card--front" aria-label="Vorderseite">
    <div class="watermark" aria-hidden="true"></div>

    <div class="brand front__brand">
      <span class="brand__dot"></span>
      <span class="brand__name">RT Gruppe</span>
    </div>

    <div class="divider"></div>

    <div class="person">
      <p class="person__name">Jonas Berger</p>
      <p class="person__role">Managing Director</p>
      <div class="person__rule"></div>
    </div>

    <ul class="contact">
      <li class="contact__item">
        <svg class="contact__icon" viewBox="0 0 16 16"><path fill="var(--orange)" d="M2 5c0-2 2-3 6-3s6 1 6 3v1h-3V5H5v1H2zM4 7h8l2 7H2z"/></svg>
        040-555-0187
      </li>
      <li class="contact__item">
        <svg class="contact__icon" viewBox="0 0 16 16"><rect x="4" y="1" width="8" height="14" rx="1.5" fill="none" stroke="var(--orange)" stroke-width="1.6"/><circle cx="8" cy="12.5" r="0.9" fill="var(--orange)"/></svg>
        040-555-0187
      </li>
      <li class="contact__item">
        <svg class="contact__icon" viewBox="0 0 16 16"><rect x="1" y="3" width="14" height="10" rx="1" fill="var(--orange)"/><path d="M1.5 3.5 8 9l6.5-5.5" fill="none" stroke="#fff" stroke-width="1.2"/></svg>
        info@rtverbund-beispiel.de
      </li>
      <li class="contact__item">
        <svg class="contact__icon" viewBox="0 0 16 16"><circle cx="8" cy="8" r="7" fill="var(--orange)"/><path d="M1 8h14M8 1c-3 3-3 11 0 14M8 1c3 3 3 11 0 14" fill="none" stroke="#fff" stroke-width="1"/></svg>
        www.rtverbund-beispiel.de
      </li>
    </ul>

    <address class="address" style="font-style:normal">
      Lindauer Weg 42<br>
      22543 Hamburg
    </address>
  </section>

</body>
</html>
```